Psychology Practice Brochure and Letterhead
Quiet Harbor Psychological Services
I will have a submission in very shortly.
Sorry for the omission of our business contact information:
26840 W. 93rd St., Suite 410
Denbury Glen, IL 60512
Phone/Fax: 708.519.2483
info@quietharborpsych.example
#2,#7 and #8
*****Please note that we have shortened the "what to expect" section and alphabetized the items under the "what we treat" section. The new wording has been uploaded and is in the brief, along with some pictures and quotes we would like you to incorporate.
Thank you so much for your hard work on our project! We really like the green curved lines of #8 because it ties all the sections together. Could you put the "do i need therapy" section on the left outside panel? Then, you can move the "what to expect" section to the middle section with a map. Also, we really like the different shades of blue that you put behind the different text sections of #2 because it makes it easier to read.Thanks
Hello designers! We are so excited about your creative ideas for the brochure.
*****Please note that we have changed the brochure wording slightly, so please edit the text in your submissions. The changes are as follows:
1) The bullet points under "What we treat" have now been alphabetized.
2)We have shortened the "what to expect" section so that it fits better with the map on the back page of the brochure. These changes are reflected in the uploaded file called "new brochure wording."
Hello designers. Please see our design brief, as we have recently uploaded photos for you to include in the brochure. Below are some quotes that we like. Feel free to include one or two in the brochure.
"A journey of a thousand miles begins with a single step." Wen Shaoli
"I am not what happens to me, I am what I choose to become." Emil Dorst
"Life is not about who you once were, it is about who you are right now, and the person you have the potential to become." Unknown
We have identified a number of photos and quotes from various sites that we might want to use, but don't want to buy them all in case they don't ultimately work in the design. Is it ok to upload them, but then buy them if they are used?
Drafts #2 and #5: Could you incorporate both blue and green?
draft #5: thank you for your submission. Could we see the design without the pictures of physicians in lab coats? Instead, we would like to see pictures of adults, children or families. Having some pictures of people looking unhappy, angry or stressed is fine along with happier pictures, as well. Any quotes about happiness or hopefulness would also be welcome.
draft #2: Thank you for your submission. Could you replace the picture of the older couple and replace it with children or teens? Also, could you show us another option for the layout on the interior? Or, another way of separating the sections that doesn't use the solid lines?
draft #1: Thank you for your submission. We like the way you've used blue and green throughout the brochure, and the addition of the tree was nice. Is there a way to reduce the quantity of brown used? Also, could you give us some additional variety in the pictures used, such as some in which the people are not jumping?
Do you have any website?
we need vector logo! please upload it!

```html
<!DOCTYPE html>
<html lang="en">
<head>
<meta charset="utf-8">
<title>Quiet Harbor Psychological Services – Brochure and Letterhead</title>
<link href="https://fonts.googleapis.com/css2?family=Libre+Baskerville:wght@400;700&family=Open+Sans:wght@400;600;700&display=swap" rel="stylesheet">
<style>
:root{
  --backdrop:#ebe8e3;
  --navy:#123a66;
  --blue:#1f5c93;
  --mid-blue:#3a7bb5;
  --light-blue:#a9c9e6;
  --pale-blue:#dbe9f5;
  --green:#4e9a2e;
  --light-green:#8cc63f;
  --placeholder:#c9d3dc;
  --white:#ffffff;
  --ink:#24384f;
}
*{margin:0;padding:0;box-sizing:border-box}
html,body{width:1200px;height:901px;overflow:hidden}
body{background:var(--backdrop);position:relative;font-family:"Open Sans",Arial,sans-serif;color:var(--ink)}
.sheet{position:absolute;background:var(--white);box-shadow:0 2px 6px rgba(0,0,0,.25);overflow:hidden}
.photo{position:absolute;background:var(--placeholder)}
.label{position:absolute;font-size:11px;color:#555;white-space:nowrap}
h2{font-family:"Libre Baskerville",Georgia,serif;font-weight:400;color:var(--white);font-size:13px;margin-bottom:4px}
p,li{font-size:5.6px;line-height:1.45}
.panel{position:absolute;top:0;height:100%}
.brand{display:flex;align-items:center;gap:6px}
.brand .dot{width:16px;height:16px;border-radius:50%;background:var(--green);flex:none}
.brand .name{font-family:"Libre Baskerville",Georgia,serif;font-weight:400;color:var(--blue);line-height:1.15}

/* outside brochure */
.outside{left:12px;top:12px;width:602px;height:441px}
.expect-box{position:absolute;left:0;top:195px;width:200px;height:246px;background:linear-gradient(var(--blue),var(--navy));padding:12px}
.expect-box p{color:#e3eefa;margin-bottom:5px}
.call{left:200px;width:201px;background:linear-gradient(var(--mid-blue),var(--navy));color:var(--white);text-align:center;padding:60px 16px 0}
.call .lead{font-family:"Libre Baskerville",Georgia,serif;font-size:11px;line-height:1.45;margin-bottom:12px}
.call .num{font-size:8px;line-height:1.6}
.call .addr{font-size:9px;margin-top:14px}
.cover{left:401px;width:201px}
.cover .brand{position:absolute;left:20px;top:262px}
.cover .brand .name{font-size:12px;width:150px}

/* inside brochure */
.inside{left:12px;top:463px;width:602px;height:420px}
.philosophy{position:absolute;left:0;top:0;width:100%;height:112px;background:linear-gradient(90deg,var(--pale-blue),var(--white))}
.philosophy .text{position:absolute;left:160px;top:10px;width:425px}
.philosophy h2,.help h2{color:var(--blue)}
.help{position:absolute;left:0;top:112px;width:100%;height:110px;background:var(--light-blue);padding:8px 12px}
.help .text{width:390px}
.help p{margin-bottom:3px}
.treat{position:absolute;left:0;top:222px;width:398px;height:198px;background:linear-gradient(var(--blue),var(--navy));padding:10px 12px}
.treat p{color:#e3eefa;margin-bottom:4px}
.treat ul{columns:2;column-gap:14px;padding-left:10px}
.treat li{color:var(--white)}
.need{position:absolute;left:398px;top:222px;width:204px;height:198px;padding:10px 12px}
.need h2{color:var(--blue)}
.need p{margin-bottom:4px}

/* front fold */
.front{left:787px;top:37px;width:116px;height:226px}
.front .band{position:absolute;left:0;top:150px;width:100%;height:76px;background:linear-gradient(var(--navy),var(--blue));padding:14px 8px}
.front .brand .name{color:var(--white);font-size:9px}
.front .brand .dot{background:var(--light-green);width:12px;height:12px}

/* letterhead */
.letterhead{left:787px;top:275px;width:408px;height:553px}
.letterhead .brand{position:absolute;left:16px;top:20px}
.letterhead .brand .name{font-size:14px;width:200px}
.letterhead .contact{position:absolute;right:16px;top:24px;text-align:right;font-size:7.5px;line-height:1.6}
.letterhead .rule{position:absolute;left:16px;right:16px;top:68px;height:2px;background:linear-gradient(90deg,var(--blue),var(--light-green))}
.letterhead .footer{position:absolute;left:150px;right:16px;bottom:22px;display:flex;gap:14px}
.letterhead .footer p{font-size:5.2px;color:var(--blue)}
.letterhead .base{position:absolute;left:0;bottom:0;width:100%;height:8px;background:linear-gradient(90deg,var(--navy),var(--blue),var(--green))}
</style>
</head>
<body>

<section class="sheet outside" aria-label="Outside of brochure">
  <div class="photo" role="img" aria-label="Photo of a person sitting under a tree in a field" style="left:0;top:0;width:200px;height:195px"></div>
  <div class="expect-box">
    <h2>What To Expect</h2>
    <p>During the first session, your psychologist will listen to the issues with which you are struggling and ask questions to better understand your situation. Together you will set goals that feel right for you and decide how often to meet.</p>
    <p>Most people see improvement within a few sessions. Each plan is shaped around your needs, your pace and your hopes for the road ahead.</p>
    <p>Sessions are kept private, and your questions are always welcome as the work goes on.</p>
  </div>
  <div class="panel call">
    <p class="lead">Take the first step toward a better tomorrow and give us a call today.</p>
    <p class="num">Phone: 708.519.2483<br>Fax: 708.519.2483</p>
    <p class="addr">26840 W. 93rd St., Suite 410<br>Denbury Glen, IL 60512</p>
  </div>
  <div class="panel cover">
    <div class="photo" role="img" aria-label="Photo of a parent lifting a smiling child" style="left:0;top:0;width:201px;height:232px"></div>
    <div class="brand"><span class="dot"></span><span class="name">Quiet Harbor Psychological Services</span></div>
  </div>
</section>
<span class="label" style="left:632px;top:364px">Outside Brochure</span>

<section class="sheet inside" aria-label="Inside of brochure">
  <div class="philosophy">
    <div class="photo" role="img" aria-label="Photo of a smiling older couple" style="left:0;top:0;width:150px;height:112px"></div>
    <div class="text">
      <h2>Philosophy</h2>
      <p>Sometimes we all need a little help getting through life's challenges. At Quiet Harbor Psychological Services, we provide a supportive, nonjudgmental environment where clients feel welcome and respected.</p>
      <p>We believe in empowering our clients and in working collaboratively with them to attain their strengths. By offering insight into your concerns and teaching you new ways to cope, we help you build resilience and move toward the life you want.</p>
    </div>
  </div>
  <div class="help">
    <div class="text">
      <h2>How We Help</h2>
      <p>We offer a range of services to help you and your family meet your goals. Individual Therapy helps you gain a better understanding of the factors contributing to your current difficulties.</p>
      <p>Child and Adolescent Therapy helps children express their emotions and behaviors in a safe and playful setting.</p>
      <p>Couples/Family Therapy explores the patterns that lead to conflict and improves communication and awareness.</p>
      <p>Parent Coaching increases parents' awareness of the factors behind their child's behavior.</p>
    </div>
    <div class="photo" role="img" aria-label="Photo of a stressed young person holding his head" style="left:410px;top:30px;width:178px;height:80px"></div>
  </div>
  <div class="treat">
    <h2>What We Treat</h2>
    <p>The decision to seek help is sometimes a difficult one. Some specific problems that we can help with are:</p>
    <ul>
      <li>Attention Deficit Hyperactivity Disorder</li>
      <li>Anxiety, Panic Attacks, Phobias</li>
      <li>Behavioral Concerns</li>
      <li>Academic Underachievement</li>
      <li>Autism Spectrum Disorders</li>
      <li>Depression/Mood Disorders</li>
      <li>Developmental and Emotional Delays</li>
      <li>Family or Relationship Conflict</li>
      <li>Stress Management/Coping Skills</li>
      <li>Parenting Education and Support</li>
      <li>Post-traumatic Stress Disorder</li>
      <li>School Refusal/Learning Difficulties</li>
      <li>Self-Esteem/Self-Worth Issues</li>
    </ul>
  </div>
  <div class="need">
    <h2>Do I Need Therapy?</h2>
    <p>Everyone experiences occasional sadness, anxiety or frustration. It may be time to seek help if you or someone you love is:</p>
    <p>Feeling overwhelmed by daily life or finding it hard to cope.</p>
    <p>Struggling in relationships at home, school or work.</p>
    <p>Noticing changes in sleep, mood or appetite that linger.</p>
    <p>"A journey of a thousand miles begins with a single step." – Wen Shaoli</p>
  </div>
</section>
<span class="label" style="left:632px;top:872px">Inside Brochure</span>

<section class="sheet front" aria-label="Front fold of brochure">
  <div class="photo" role="img" aria-label="Photo of a family playing together outdoors" style="left:0;top:0;width:116px;height:150px"></div>
  <div class="band">
    <div class="brand"><span class="dot"></span><span class="name">Quiet Harbor Psychological Services</span></div>
  </div>
</section>
<span class="label" style="left:800px;top:306px">Front Fold</span>

<section class="sheet letterhead" aria-label="Letterhead">
  <div class="brand"><span class="dot"></span><span class="name">Quiet Harbor Psychological Services</span></div>
  <div class="contact">Phone 708.519.2483<br>Fax 708.519.2483<br>info@quietharborpsych.example</div>
  <div class="rule"></div>
  <div class="footer">
    <p>Individual Therapy<br>Child and Adolescent Therapy<br>Couples and Family Therapy<br>Parent Coaching</p>
    <p>Anxiety and Mood Concerns<br>Stress Management<br>Behavioral Concerns<br>Self-Esteem Support</p>
    <p>26840 W. 93rd St., Suite 410<br>Denbury Glen, IL 60512<br>708.519.2483</p>
  </div>
  <div class="base"></div>
</section>
<span class="label" style="left:718px;top:785px">Letterhead</span>

</body>
</html>
```